KVAP Property Flyer - For Support Coordinators

Revamping our current brochures and social media posts for our properties. We need a clearer, simpler design that would be designed for Support Coordinators. Attached is our current brochure for reference.

Key details to highlight would include:
- Type of property: Studio Apartments with Psychosocial Disability Support located in Inner West
- Accommodation features
- Services

Our logo is also attached, please make the brochure with similar branding colours and fonts.

Designs look the same

Sick

Font styles to use
Sans Serif
Other font styles liked:
• Montserrat Light and Montserrat Semi Bold

Colors
0054AA
0677BA
7BADD7
CADEEF
E8F1F8

Requirements
Nice to have
• Please refer to this style guide: https://slides.trovelmark.com/deck/8TkwPzLmRd5VbQx2NcYh4GfJs7AeUo9WiKnBrMp3tZq/view?mode=shared

```html
<!DOCTYPE html>
<html lang="en">
<head>
<meta charset="utf-8">
<title>Kindred Harbour Care – Petersham Studio Apartments</title>
<link rel="stylesheet" href="https://fonts.googleapis.com/css2?family=Inter:wght@800&family=Arimo:wght@400;700&display=swap">
<style>
  :root {
    --ink: #2b303a;
    --ink-deep: #26292f;
    --text: #1f2228;
    --blue: #2c86c0;
    --blue-soft: #4a9bcb;
    --paper: #ffffff;
    --panel: rgba(240, 244, 248, 0.93);
    --rule: #c9cdd2;
  }
  * { box-sizing: border-box; margin: 0; padding: 0; }
  html, body { width: 1200px; height: 1200px; overflow: hidden; background: var(--paper); }
  body { position: relative; font-family: "Arimo", Arial, sans-serif; color: var(--ink); }

  .flyer {
    position: absolute; left: 205px; top: 88px; width: 796px; height: 1031px;
    background: var(--paper); box-shadow: 0 0 6px rgba(0,0,0,0.12); overflow: hidden;
  }

  .hero-photo {
    position: absolute; left: 0; top: 0; width: 796px; height: 521px;
    background: linear-gradient(180deg, #78abdc 0%, #9cc2e6 28%, #8f969e 48%, #4f4c4c 64%, #6b6358 80%, #9a958c 100%);
  }

  .brand-panel {
    position: absolute; left: 34px; top: 0; width: 256px; height: 362px;
    background: var(--panel);
    clip-path: polygon(0 0, 100% 0, 100% 324px, 0 100%);
    text-align: center;
  }
  .brand-dot {
    position: absolute; left: 98px; top: 84px; width: 60px; height: 60px;
    border-radius: 50%; background: var(--blue-soft);
  }
  .brand-name {
    position: absolute; left: 0; right: 0; top: 166px;
    font-size: 15px; line-height: 18px; letter-spacing: 1.2px; color: #4a4f57; text-transform: uppercase; white-space: nowrap;
  }
  .suburb {
    position: absolute; left: 0; right: 0; top: 196px;
    font-family: "Inter", Arial, sans-serif; font-weight: 800; font-size: 33px; line-height: 40px;
    color: var(--ink); letter-spacing: -1px;
  }
  .tagline {
    position: absolute; left: 0; right: 0; top: 247px;
    font-size: 19px; line-height: 23.5px; color: var(--text);
  }

  .address-pill {
    position: absolute; left: 519px; top: 34px; width: 290px; height: 22px;
    background: var(--paper); border-radius: 11px 0 0 11px;
    display: flex; align-items: center; padding-left: 14px; gap: 6px;
    font-size: 11px; font-weight: 700; color: var(--ink-deep);
  }

  .welcome {
    position: absolute; left: 34px; top: 436px; width: 728px; height: 160px;
    background: var(--ink); border-radius: 28px 28px 0 0; color: #fff; text-align: center;
    padding: 14px 18px 0;
  }
  .welcome h1 {
    font-family: "Inter", Arial, sans-serif; font-weight: 800; font-size: 25px; line-height: 30px;
    letter-spacing: -0.8px; margin-bottom: 10px;
  }
  .welcome p { font-size: 12.5px; line-height: 15.6px; }
  .welcome p + p { margin-top: 16px; }

  .info-column { position: absolute; top: 609px; }
  .info-column.community { left: 34px; width: 370px; }
  .info-column.features { left: 492px; width: 290px; }
  .info-column h2 {
    font-family: "Inter", Arial, sans-serif; font-weight: 800; font-size: 22px; line-height: 26px;
    letter-spacing: -0.9px; color: var(--ink); white-space: nowrap;
  }
  .info-column h2::after {
    content: ""; display: block; width: 62px; height: 3px; background: var(--blue); margin-top: 1px;
  }
  .info-list { list-style: none; margin-top: 8px; }
  .info-list li {
    display: flex; align-items: flex-start; gap: 6px; font-size: 12.5px; line-height: 15.6px; min-height: 32.5px; color: var(--text);
  }
  .info-list svg { flex: none; width: 15px; height: 15px; }
  .column-rule { position: absolute; left: 412px; top: 612px; width: 2px; height: 137px; background: var(--rule); }

  .gallery-band { position: absolute; left: 0; top: 820px; width: 796px; height: 46px; background: var(--ink); }
  .gallery-frame {
    position: absolute; top: 759px; width: 230px; height: 157px; background: var(--paper);
    padding: 4px; box-shadow: 0 0 3px rgba(0,0,0,0.2);
  }
  .gallery-frame .photo { width: 100%; height: 100%; }
  .frame-1 { left: 33px; } .frame-2 { left: 281px; } .frame-3 { left: 530px; }
  .frame-1 .photo { background: linear-gradient(110deg, #8d7f75 0%, #d8d8d6 35%, #eeeeec 60%, #4a4a4c 100%); }
  .frame-2 .photo { background: linear-gradient(90deg, #d4d6d8 0%, #b9bcbf 45%, #3c3d3f 62%, #55565a 100%); }
  .frame-3 .photo { background: linear-gradient(90deg, #eeefef 0%, #dcdee0 45%, #2f3032 58%, #c9cdd1 75%, #e4e6e7 100%); }

  .contact-bar { position: absolute; left: 0; top: 918px; width: 796px; height: 113px; background: var(--ink-deep); }
  .cta {
    position: absolute; left: 301px; top: 934px; width: 194px; height: 36px;
    background: linear-gradient(180deg, #4ea0cf, #3686b8); border-radius: 8px;
    color: #fff; font-size: 17px; text-align: center; line-height: 36px;
  }
  .contacts {
    position: absolute; left: 34px; top: 986px; width: 733px; display: flex; justify-content: space-between; align-items: center;
    color: #fff; font-size: 14px;
  }
  .contacts span { display: flex; align-items: center; gap: 6px; white-space: nowrap; }
  .contacts .strong { font-weight: 700; }
  .contacts svg { width: 11px; height: 11px; }
</style>
</head>
<body>
<main class="flyer">
  <div class="hero-photo" role="img" aria-label="Street photo of a dark brick four-storey apartment building with planted balconies beside older homes under a blue sky"></div>

  <section class="brand-panel">
    <span class="brand-dot"></span>
    <div class="brand-name">Kindred Harbour Care</div>
    <div class="suburb">PETERSHAM</div>
    <p class="tagline">Studio Apartments for<br>people with a<br>psychosocial disability.</p>
  </section>

  <div class="address-pill">
    <svg width="10" height="12" viewBox="0 0 10 12"><path d="M5 0a4 4 0 0 1 4 4c0 3-4 8-4 8S1 7 1 4a4 4 0 0 1 4-4z" fill="#2c86c0"/><circle cx="5" cy="4" r="1.5" fill="#fff"/></svg>
    18 Larkin Street, Petersham NSW 2049
  </div>

  <section class="welcome">
    <h1>WELCOME TO PETERSHAM</h1>
    <p>Located in the heart of Petersham, our new 20 self-contained studio apartments which have a kitchen with fridge, small stove top and microwave. It has a single bed, tv, dining table and bathroom. Some apartments have small balconies, and some have decks overlooking the bustling suburb.</p>
    <p>Situated a 5 minute walk to Petersham Train Station, and other public transport.</p>
  </section>

  <section class="info-column community">
    <h2>COMMUNITIES &amp; FACILITIES</h2>
    <ul class="info-list">
      <li><svg viewBox="0 0 16 16"><path d="M2 8l6-6 6 6v6H2z" fill="none" stroke="#2c86c0" stroke-width="1.2"/></svg>Close to shops, cafes and public transport.</li>
      <li><svg viewBox="0 0 16 16"><circle cx="5" cy="4" r="2" fill="none" stroke="#2c86c0" stroke-width="1.2"/><circle cx="11" cy="4" r="2" fill="none" stroke="#2c86c0" stroke-width="1.2"/><path d="M2 15V9h6v6M8 15V9h6v6" fill="none" stroke="#2c86c0" stroke-width="1.2"/></svg>Local GP Practice and Dentistry.</li>
      <li><svg viewBox="0 0 16 16"><circle cx="4" cy="5" r="2" fill="none" stroke="#2c86c0" stroke-width="1.2"/><circle cx="8" cy="4" r="2" fill="none" stroke="#2c86c0" stroke-width="1.2"/><circle cx="12" cy="5" r="2" fill="none" stroke="#2c86c0" stroke-width="1.2"/><path d="M1 14c1-4 13-4 14 0z" fill="none" stroke="#2c86c0" stroke-width="1.2"/></svg>Commercial Space for Social Enterprise.</li>
    </ul>
  </section>

  <div class="column-rule"></div>

  <section class="info-column features">
    <h2>FEATURES &amp; SERVICES</h2>
    <ul class="info-list">
      <li><svg viewBox="0 0 16 16"><circle cx="8" cy="8" r="6.5" fill="none" stroke="#2c86c0" stroke-width="1.2"/><circle cx="8" cy="8" r="4" fill="none" stroke="#2c86c0" stroke-width="0.8"/></svg>24/7 Video-Intercom &amp; on site support.</li>
      <li><svg viewBox="0 0 16 16"><circle cx="7" cy="2.5" r="1.5" fill="#2c86c0"/><path d="M7 5v5h4l2 4" fill="none" stroke="#2c86c0" stroke-width="1.2"/><circle cx="7" cy="11" r="4" fill="none" stroke="#2c86c0" stroke-width="1.2"/></svg>Disability access walkways &amp; bathroom.</li>
      <li><svg viewBox="0 0 16 16"><circle cx="8" cy="5" r="3" fill="none" stroke="#2c86c0" stroke-width="1.2"/><path d="M2 15c0-4 12-4 12 0" fill="none" stroke="#2c86c0" stroke-width="1.2"/></svg>Trained &amp; experienced Staff in<br>psychosocial disability.</li>
    </ul>
  </section>

  <div class="gallery-band"></div>
  <figure class="gallery-frame frame-1"><div class="photo" role="img" aria-label="Studio interior with single bed, window and kitchenette"></div></figure>
  <figure class="gallery-frame frame-2"><div class="photo" role="img" aria-label="Open fridge beside dark kitchen benchtop with stove top"></div></figure>
  <figure class="gallery-frame frame-3"><div class="photo" role="img" aria-label="Bright studio with wall-mounted tv and glass doors to a balcony"></div></figure>

  <footer>
    <div class="contact-bar"></div>
    <div class="cta">FIND OUT MORE:</div>
    <div class="contacts">
      <span class="strong"><svg viewBox="0 0 12 12"><rect x="0.5" y="2" width="11" height="8" fill="#2c86c0"/><path d="M0.5 2l5.5 4.5L11.5 2" fill="none" stroke="#26292f" stroke-width="1"/></svg>info@kindredharbour.com.au</span>
      <span class="strong"><svg viewBox="0 0 12 12"><circle cx="6" cy="6" r="5" fill="none" stroke="#2c86c0" stroke-width="1.2"/><path d="M1 6h10M6 1c-3 3-3 7 0 10M6 1c3 3 3 7 0 10" fill="none" stroke="#2c86c0" stroke-width="0.9"/></svg>www.kindredharbour.com.au</span>
      <span><svg viewBox="0 0 12 12"><path d="M2 1l2.5 0 1 3-1.5 1c.8 1.5 1.5 2.2 3 3l1-1.5 3 1V11C6 11 1 6 1 2z" fill="#2c86c0"/></svg>1300 555 018</span>
      <span><svg viewBox="0 0 12 12"><circle cx="6" cy="6" r="5.5" fill="#2c86c0"/></svg>kindredharbour_homes</span>
    </div>
  </footer>
</main>
</body>
</html>
```